Visitenkarten für Elektro- und Informationstechnik-Betrieb
Zielgruppe
Wir sind ein Elektro- und Informationstechnik-Betrieb.
Unsere Fachgebiete sind Photovoltaikanlagen, Stromspeicher, Smart-Home und Ladestationrn
Aufgabenstellung
Design in der Farben des Logos und ein dunkler Hintergrund.

```html
<!DOCTYPE html>
<html lang="de">
<head>
<meta charset="utf-8">
<title>Visitenkarte Strovani Elektrotechnik</title>
<link href="https://fonts.googleapis.com/css2?family=Ubuntu:wght@400;500;700&display=swap" rel="stylesheet">
<style>
  :root {
    --page: #fefefe;
    --card: #000000;
    --copper: #c0714a;
    --steel: #5b8ea8;
    --shadow-mark: #262626;
  }
  * { margin: 0; padding: 0; box-sizing: border-box; }
  html, body {
    width: 848px; height: 1200px; overflow: hidden;
    background: var(--page);
    font-family: "Ubuntu", sans-serif;
  }
  .card {
    position: absolute;
    left: 254px;
    width: 344px;
    height: 222px;
    background: var(--card);
  }
  .card--front { top: 323px; }
  .card--back { top: 568px; height: 221px; }

  .brand {
    position: absolute; left: 20px; top: 36px;
    display: flex; align-items: center; gap: 7px;
  }
  .brand__dot {
    width: 14px; height: 14px; border-radius: 50%;
    background: var(--copper);
  }
  .brand__name {
    color: var(--copper);
    font-weight: 700;
    font-size: 15px;
    letter-spacing: 0.2px;
  }

  .backdrop-mark {
    position: absolute; left: 171px; top: 62px;
    width: 155px; height: 150px;
    background: radial-gradient(ellipse at 60% 45%, var(--shadow-mark) 0%, rgba(38,38,38,0.5) 55%, rgba(0,0,0,0) 80%);
  }

  .contact {
    position: absolute; left: 20px; top: 97px;
    color: var(--copper);
    font-size: 10px;
    line-height: 13px;
  }
  .contact__name {
    color: var(--steel);
    font-weight: 700;
    font-size: 12.5px;
    letter-spacing: 0.3px;
    line-height: 14px;
  }
  .contact__role { margin-bottom: 4px; }
  .contact__address { margin-bottom: 4px; }
  .contact__phone {
    display: flex; align-items: center; gap: 2px;
    margin-bottom: 4px;
  }
  .contact__phone svg { width: 12px; height: 12px; }
</style>
</head>
<body>
  <section class="card card--front">
    <div class="brand">
      <span class="brand__dot"></span>
      <span class="brand__name">Strovani Elektrotechnik</span>
    </div>

    <div class="backdrop-mark" role="img" aria-label="Dezentes Markenzeichen als Hintergrunddekor"></div>

    <div class="contact">
      <p class="contact__name">JORIN VELT</p>
      <p class="contact__role">Geschäftsführer</p>
      <p class="contact__address">Am Lindgraben 7<br>54321 Talheim</p>
      <p class="contact__phone">
        <svg viewBox="0 0 24 24" aria-hidden="true"><path fill="#c0714a" d="M6.6 10.8a15.1 15.1 0 0 0 6.6 6.6l2.2-2.2c.3-.3.7-.4 1-.2 1.1.4 2.3.6 3.6.6.6 0 1 .4 1 1V20c0 .6-.4 1-1 1A17 17 0 0 1 3 4c0-.6.4-1 1-1h3.5c.6 0 1 .4 1 1 0 1.3.2 2.5.6 3.6.1.3 0 .7-.2 1z"/></svg>
        +49 151 000 482 16
      </p>
      <p>service@strovani-elektro.example</p>
      <p>www.strovani-elektro.example</p>
    </div>
  </section>

  <section class="card card--back"></section>
</body>
</html>
```